Web application design for investigative software

ClueVane is an investigation web application that would organize, create visualizations and allow collaboration. It’s available to anyone and can be used by students, historians, watchdog groups, civic hackers, investigative reporters, mystery enthusiasts, authors, even conspiracy theorists.

We are looking for two related pages. The first, a splash, or front, page and the second a ‘template’ for the web application. They should both be styled the same. The only restriction is that the logo is set.

The design should also be modern and visually well organized — employing a combination of visual devices and info graphics. Keep it light and not too heavy but strong/ professional. Do not be influenced by the current colors of cluevane-example.com, though the colors should be compatible with the logo..

The pages should be compatible with bootstrap, mostly for it’s JS and component functionality. It can be advised by the designer that a subset of bootstrap be used.

The splash page.
Something along the lines of (though not a copy of) :
https://www.plorvex-example.com/advertise
http://www.brimtallhost-example.net/
http://www.corvilode-example.com/
http://www.fennaquist-example.com/

I have a very rough wire frame ish html file uploaded. Use a a guide, but alternate ideas are encouraged.

The application page should have some sort of bar for at the top for system level links a header and a footer. A vertical column to the left between the header and footer for ads, though this will be dynamic as a user can pay out of seeing adds. All dynamic actions will be made by the developers at ClueVane.

WARNING. Please do not submit pre-made templates from some template website. We can do that ourselves for free.

This project will deliver CODE. HTML, CSS and supporting graphics and files.

```html
<!DOCTYPE html>
<html lang="en">
<head>
<meta charset="utf-8">
<title>ClueVane – Investigation web application</title>
<link rel="stylesheet" href="https://fonts.googleapis.com/css2?family=Poiret+One&family=Open+Sans:wght@400;600&display=swap">
<style>
:root{
  --red:#d8392b;
  --red-dark:#b52a1f;
  --salmon:#e58a7c;
  --text:#333333;
  --muted:#9a9a9a;
  --grey-box:#b9b9b9;
  --hero-top:#ffffff;
  --hero-bottom:#ececec;
  --footer-bg:#e9e9e9;
  --footer-text:#888888;
  --white:#ffffff;
}
*{box-sizing:border-box;margin:0;padding:0}
html,body{width:1006px;height:1200px;overflow:hidden;background:var(--white)}
body{font-family:"Open Sans",sans-serif;color:var(--text);position:relative}
.page{position:relative;width:1006px;height:1200px;overflow:hidden}

/* hero */
.hero{position:absolute;left:0;top:0;width:1006px;height:360px;
  background:linear-gradient(var(--hero-top),var(--hero-bottom));
  border-bottom:2px solid var(--salmon)}
.masthead{position:absolute;left:134px;top:0;width:738px;height:92px}
.masthead-curve{position:absolute;left:0;top:0}
.brand{position:absolute;left:14px;top:20px;display:flex;align-items:center;gap:8px}
.brand-mark{width:36px;height:36px;border-radius:50%;background:var(--red)}
.brand-name{font-family:"Poiret One",sans-serif;font-size:27px;font-weight:400;color:var(--red)}
.main-nav{position:absolute;left:232px;top:0;display:flex;font-size:13px}
.main-nav a{color:var(--text);text-decoration:none;padding:12px 9px 0;height:42px}
.main-nav a.active{background:var(--red);color:var(--white);margin-right:6px}
.account{position:absolute;right:5px;top:0;display:flex;font-size:11px}
.account a{color:var(--white);text-decoration:none;padding:2px 8px;height:19px}
.account .login{background:var(--red-dark)}
.account .register{background:var(--salmon)}
.social{position:absolute;right:5px;top:36px;display:flex;gap:4px}
.social span{display:block;width:18px;height:18px;background:var(--red-dark);opacity:.85}

.hero-copy{position:absolute;left:135px;top:127px;width:360px;font-family:"Poiret One",sans-serif;color:#444}
.hero-copy h1{font-size:22px;font-weight:400;letter-spacing:.3px}
.hero-copy .lead{font-size:17px;line-height:20px;margin-top:6px}
.hero-copy p{font-size:14px;line-height:18px;margin-top:18px;font-weight:600}
.hero-copy a{color:var(--red)}
.hero-art{position:absolute;left:470px;top:62px;width:400px;height:298px;
  background:radial-gradient(circle at 55% 45%,#f0c419 0 18%,#5fbf2a 18% 36%,#e52b1f 36% 52%,#3d7fe0 52% 66%,rgba(0,0,0,0) 67%)}

/* features */
.features{position:absolute;left:136px;top:362px;width:734px;height:216px}
.feature{position:absolute;top:0;width:222px;height:216px;text-align:center;color:var(--white);
  font-family:"Poiret One",sans-serif}
.feature.organize{left:0;background:var(--red)}
.feature.visualize{left:256px;background:var(--grey-box)}
.feature.collaborate{left:512px;background:var(--grey-box)}
.feature svg{margin-top:28px}
.feature h2{font-size:20px;font-weight:400;margin-top:8px}
.feature p{font-size:11px;line-height:14px;font-weight:600;margin:8px 22px 0}
.feature .join{font-size:19px;text-decoration:underline;margin-top:16px;display:block;color:var(--white)}

/* content */
.content{position:absolute;left:135px;top:608px;width:736px}
.intro{font-family:"Poiret One",sans-serif;font-size:14px;line-height:18px;font-weight:600;color:#222}
.content h2{font-family:"Poiret One",sans-serif;font-weight:400;font-size:28px;color:var(--red);margin-top:18px}
.content .note{font-size:10px;line-height:16px;color:var(--muted);margin-top:8px}
.content .note + .note{margin-top:12px}

/* footer */
.site-footer{position:absolute;left:0;top:1028px;width:1006px;height:172px;background:var(--footer-bg);
  border-top:3px solid var(--salmon);font-size:11px;color:var(--footer-text)}
.footer-col{position:absolute;top:16px}
.footer-col h3{font-size:13px;font-weight:400;color:var(--red-dark);margin-bottom:8px}
.footer-col ul{list-style:none;line-height:14px}
.contact{left:135px}
.contact li{display:flex;gap:10px;align-items:flex-start;margin-bottom:13px;line-height:15px}
.links-direct{left:390px}
.links-related{left:570px}
.connect{left:772px}
.connect .social{position:static;margin-top:2px}
.copyright{position:absolute;left:135px;top:143px;color:var(--red-dark);font-size:11px}
</style>
</head>
<body>
<div class="page">

  <header class="hero">
    <div class="masthead">
      <svg class="masthead-curve" width="738" height="92" viewBox="0 0 738 92" aria-hidden="true">
        <path d="M0 0 H738 V80 Q560 36 300 50 Q120 62 0 86 Z" fill="#ffffff"/>
        <path d="M0 86 Q120 62 300 50 Q560 36 738 80" fill="none" stroke="#cfcfcf" stroke-width="2"/>
      </svg>
      <div class="brand"><span class="brand-mark"></span><span class="brand-name">ClueVane</span></div>
      <nav class="main-nav">
        <a class="active" href="#">Home</a><a href="#">About</a><a href="#">Services</a><a href="#">Portfolio</a><a href="#">FAQ</a><a href="#">Contact</a>
      </nav>
      <div class="account"><a class="login" href="#">Login</a><a class="register" href="#">Register</a></div>
      <div class="social"><span></span><span></span><span></span><span></span></div>
    </div>

    <div class="hero-copy">
      <h1>Investigation web application</h1>
      <p class="lead">We would organize, create visualizations and allow collaboration.</p>
      <p>It's available to anyone and can be used by students, historians, watchdog groups, civic hackers, investigative reporters, mystery enthusiasts, authors, even conspiracy theorists. <a href="#">Read More</a></p>
    </div>
    <div class="hero-art" role="img" aria-label="Four interlocking 3D puzzle pieces labelled Track, Relate, Solve! and Investigate in yellow, green, red and blue"></div>
  </header>

  <section class="features">
    <div class="feature organize">
      <svg width="72" height="72" viewBox="0 0 72 72" aria-hidden="true">
        <circle cx="36" cy="36" r="33" fill="none" stroke="#fff" stroke-width="3"/>
        <path d="M36 20 L48 42 H24 Z" fill="none" stroke="#fff" stroke-width="4" stroke-linejoin="round"/>
      </svg>
      <h2>Organize</h2>
      <p>ClueVane is an on-line system that allows you to enter what you know about a person, event, object, or group.</p>
    </div>
    <div class="feature visualize">
      <svg width="72" height="72" viewBox="0 0 72 72" aria-hidden="true">
        <circle cx="36" cy="36" r="33" fill="#fff" stroke="#8a8a8a" stroke-width="3"/>
        <text x="36" y="49" text-anchor="middle" font-family="Open Sans,sans-serif" font-weight="600" font-size="38" fill="#8a8a8a">?</text>
      </svg>
      <h2>Visualize</h2>
      <p>Once data has been entered, use ClueVane's graphical analysis tools to analyze your data in new ways.</p>
    </div>
    <div class="feature collaborate">
      <svg width="72" height="72" viewBox="0 0 72 72" aria-hidden="true">
        <circle cx="36" cy="36" r="33" fill="#fff" stroke="#8a8a8a" stroke-width="3"/>
        <path d="M23 37 L32 46 L50 25" fill="none" stroke="#8a8a8a" stroke-width="6" stroke-linecap="round"/>
      </svg>
      <h2>Collaborate</h2>
      <a class="join" href="#">Join with others</a>
    </div>
  </section>

  <main class="content">
    <p class="intro">Have you ever compiled a lot of data about something, but been unable to figure out what it means? Often, the number of people involved, the number of events at which they might have met, and the number of common contacts are just too much for a person to track. This can happen when you are trying to understand the players and interests in current events, or the characters and actions in a novel. It's easy to collect the data, but hard to visualize it or analyze the relationships.<br>This is where ClueVane comes in. ClueVane allows you to easily visualize people, events, things, groups, and timelines and to easily see the relationships between them.</p>

    <h2>How does ClueVane work?</h2>
    <p class="note">Once data has been entered, use ClueVane's graphical analysis tools to analyze your data in new ways. Use relationship maps to find out how two people or groups are associated. Use timeline analysis to show cause and effect of seemingly unrelated events.</p>
    <p class="note">Use social network mapping to show how relationships change over time. Look for events that stand out or relationships that have great impact on multiple events. Like a spider's web, look for the intersections that matter, then look for the players that brought that intersection into focus.</p>

    <h2>What do I get with ClueVane?</h2>
    <p class="note">Basic ClueVane will allow any registered user to create, maintain and analyze one investigation. Advanced features will be available a la carte and will include special analytical reports, multiple investigations, and the ability to share an investigation among multiple users. Investigations of general interest could also be shared publicly in read-only mode.</p>
    <p class="note">You will also get access to several read-only public investigations to use as a model. These might include the plots of popular novels or movies, the details of a major political event, or an investigation into a famous crime.</p>
  </main>

  <footer class="site-footer">
    <div class="footer-col contact">
      <h3>Contact Us</h3>
      <ul>
        <li><svg width="14" height="12" viewBox="0 0 14 12" aria-hidden="true"><rect x="1" y="2" width="12" height="9" fill="none" stroke="#888" stroke-width="1.5"/><path d="M1 2 L7 7 L13 2" fill="none" stroke="#888" stroke-width="1.5"/></svg>info@cluevane-example.com</li>
        <li><svg width="14" height="16" viewBox="0 0 14 16" aria-hidden="true"><rect x="3" y="1" width="8" height="14" rx="1.5" fill="none" stroke="#888" stroke-width="1.5"/><circle cx="7" cy="12.5" r="1" fill="#888"/></svg>+91 900-555-0142</li>
        <li><svg width="14" height="18" viewBox="0 0 14 18" aria-hidden="true"><path d="M7 17 C3 11 1 8 1 6 A6 6 0 0 1 13 6 C13 8 11 11 7 17 Z" fill="#888"/><circle cx="7" cy="6" r="2" fill="#e9e9e9"/></svg><span>ClueVane, Company Address<br>Jaipur City, India</span></li>
      </ul>
    </div>
    <div class="footer-col links-direct">
      <h3>Direct Links</h3>
      <ul><li>Home</li><li>About</li><li>Services</li><li>Portfolio</li><li>Contact</li></ul>
    </div>
    <div class="footer-col links-related">
      <h3>Related Links</h3>
      <ul><li>Live Chat</li><li>Recent News</li><li>FAQ</li></ul>
    </div>
    <div class="footer-col connect">
      <h3>Connect with us</h3>
      <div class="social"><span></span><span></span><span></span><span></span></div>
    </div>
    <p class="copyright">© 2014 &nbsp;cluevane-example.com</p>
  </footer>

</div>
</body>
</html>
```